Business Card for Wellness Clinic

We need a business card for our new logo. I want it to match the feel of the logo

Target Market(s)

Young professional families looking for holistic health care

Industry/Entity Type

Health And Wellness

Contact Information for Business Card

Our business Name: Brackenfield Health & wellness Centre, our phone #, email address...see attached old business card

Font styles to use
Sans Serif

Colors
33b8a4
cee9f5

Requirements
Must have
• my logo and business name
• Font is "Helvetica Neue LT Std 45 Light" and
• Only for "&" using font "Trajan pro bold"
• Use colors in the logo

```html
<!DOCTYPE html>
<html lang="en">
<head>
<meta charset="utf-8">
<title>Brackenfield Health &amp; wellness Centre – Business Card</title>
<link rel="stylesheet" href="https://fonts.googleapis.com/css2?family=Roboto:wght@300;400&family=Alegreya:wght@400;500&display=swap">
<style>
  :root {
    --teal: #3db4a3;
    --teal-deep: #33a897;
    --ink: #5a5a5a;
    --rule: #6b6b6b;
    --paper: #ffffff;
    --backdrop: #ececec;
    --white: #ffffff;
  }
  * { box-sizing: border-box; margin: 0; padding: 0; }
  html, body {
    width: 1200px; height: 1200px; overflow: hidden;
    background: var(--backdrop);
    font-family: "Roboto", Arial, sans-serif;
  }
  .canvas { position: relative; width: 1200px; height: 1200px; }

  .card {
    position: absolute; left: 238px; width: 712px; height: 420px; overflow: hidden;
  }
  .card--appointment { top: 118px; background: var(--paper); }
  .card--contact { top: 642px; background: var(--teal); color: var(--white); }

  /* brand */
  .brand { position: absolute; display: flex; align-items: center; gap: 22px; }
  .brand__mark { width: 60px; height: 60px; background: var(--teal); flex: none; }
  .brand__name {
    font-family: "Roboto", Arial, sans-serif; font-weight: 300;
    font-size: 21px; letter-spacing: 4px; line-height: 1.45; text-transform: uppercase;
  }
  .card--appointment .brand { left: 120px; top: 62px; }
  .card--appointment .brand__name { color: var(--ink); }
  .card--contact .brand { left: 30px; top: 46px; flex-direction: column; align-items: center; gap: 20px; width: 330px; }
  .card--contact .brand__mark { background: var(--white); width: 64px; height: 64px; }
  .card--contact .brand__name { color: var(--white); text-align: center; }

  /* appointment fields */
  .field-row {
    position: absolute; left: 40px; right: 40px;
    display: flex; align-items: flex-end; gap: 6px;
    font-size: 20px; color: var(--ink);
  }
  .field-row--date { top: 208px; }
  .field-row--for { top: 266px; }
  .field-line { border-bottom: 1.5px solid var(--rule); height: 18px; }
  .field-line--date { flex: 1 1 auto; margin-right: 6px; }
  .field-line--time { width: 150px; }
  .field-line--for { flex: 1 1 auto; }

  .policy-band {
    position: absolute; left: 0; right: 0; bottom: 0; height: 74px;
    background: var(--teal); color: var(--white);
    display: flex; align-items: center; justify-content: center;
    text-align: center; font-size: 18px; line-height: 1.3;
  }

  /* contact side */
  .person {
    position: absolute; right: 36px; top: 222px; text-align: right;
    font-family: "Alegreya", Georgia, serif;
  }
  .person__name { font-size: 27px; font-weight: 500; }
  .person__role { font-size: 18px; margin-top: 6px; }
  .divider { position: absolute; left: 30px; top: 274px; width: 444px; border-top: 1.5px solid var(--white); }

  .contact-list {
    position: absolute; left: 30px; top: 304px; list-style: none;
    font-family: "Alegreya", Georgia, serif; font-size: 18px;
  }
  .contact-list li { display: flex; align-items: center; gap: 16px; height: 26.5px; }
  .contact-list svg { width: 19px; height: 16px; flex: none; }

  .address {
    position: absolute; right: 36px; top: 331px; text-align: right;
    font-family: "Alegreya", Georgia, serif; font-size: 18px; line-height: 26.5px; font-style: normal;
  }
</style>
</head>
<body>
<main class="canvas">

  <section class="card card--appointment" aria-label="Appointment card">
    <div class="brand">
      <span class="brand__mark"></span>
      <p class="brand__name">Brackenfield Health<br>&amp; wellness Centre</p>
    </div>

    <div class="field-row field-row--date">
      <span>Date:</span><span class="field-line field-line--date"></span>
      <span>Time :</span><span class="field-line field-line--time"></span>
    </div>
    <div class="field-row field-row--for">
      <span>For:</span><span class="field-line field-line--for"></span>
    </div>

    <p class="policy-band">If you are unable to keep your appointment, please provide<br>at least 2 business days notice or full visit fees will apply.</p>
  </section>

  <section class="card card--contact" aria-label="Contact card">
    <div class="brand">
      <span class="brand__mark"></span>
      <p class="brand__name">Brackenfield Health<br>&amp; wellness Centre</p>
    </div>

    <div class="person">
      <p class="person__name">Dr. Maren Holloway, N.D.</p>
      <p class="person__role">Naturopathic Doctor</p>
    </div>
    <span class="divider"></span>

    <ul class="contact-list">
      <li>
        <svg viewBox="0 0 20 16" aria-hidden="true"><path fill="#fff" d="M2 5c0-2 3-3 8-3s8 1 8 3v2h-4V5.5c-1-.5-2.5-.7-4-.7s-3 .2-4 .7V7H2z"/><path fill="#fff" d="M5 8h10l2 6H3z"/><circle cx="10" cy="11" r="1.6" fill="#3db4a3"/></svg>
        <span>613-555-0142</span>
      </li>
      <li>
        <svg viewBox="0 0 20 16" aria-hidden="true"><rect x="1" y="2" width="18" height="12" fill="#fff"/><path d="M1 2l9 7 9-7M1 14l7-6M19 14l-7-6" fill="none" stroke="#3db4a3" stroke-width="1.3"/></svg>
        <span>mholloway@brackenfieldnd.ca</span>
      </li>
      <li>
        <svg viewBox="0 0 20 16" aria-hidden="true"><circle cx="10" cy="8" r="7" fill="#fff"/><g fill="none" stroke="#3db4a3" stroke-width="1"><ellipse cx="10" cy="8" rx="3" ry="7"/><path d="M3 8h14M4.5 4.5h11M4.5 11.5h11"/></g></svg>
        <span>www.brackenfieldnd.ca</span>
      </li>
    </ul>

    <address class="address">48 Linden Row W, Suite 310<br>Ottawa, ON K2P 3L7</address>
  </section>

</main>
</body>
</html>
```